KitVarro.com FACELIFT design for the online store

A) GENERAL
We need a small FACELIFT design with a short styleguide for our online store http://KitVarro.com (online store for sport goods; the store is just now in responsive design; actually only in German). The store is the first online store worldwide with 3d images for all products.
B) Designers: PLEASE NOTE:
- We don't want change functionality!
- We only want a small facelift.
- We don't need a fully coded website.
C) We only need for the responsive design views:
1. the home page design (one page)
http://www.kitvarro.com/de/
2. the category listing design (one page)
http://www.kitvarro.com/de/alle/running.html
3. the product detail page (one page)
http://www.kitvarro.com/de/pembrik-tz-flo-3d-hvx-herren-traillaufschuhe-drelon-wex.html
4. the cms page (textonly !!!)
http://www.kitvarro.com/de/versand-und-lieferung
5. the Mega drop down
D) We intend to change/use:
- maybe to use a background image in the start page, and each category
- change the header
- change the font sizes for the titles (maybe in capital letters)
- change the mega drop down
Europe
Store
4 page

```html
<!DOCTYPE html>
<html lang="de">
<head>
<meta charset="utf-8">
<title>KitVarro.com – Startseite</title>
<link rel="stylesheet" href="https://fonts.googleapis.com/css2?family=Open+Sans:wght@400;600;700;800&display=swap">
<style>
:root{
  --red:#e3173e;
  --red-dark:#b80f2e;
  --ink:#1c1c1c;
  --dark:#222326;
  --darker:#141414;
  --grey:#6f6f6f;
  --line:#dedede;
  --light:#f2f2f2;
  --white:#ffffff;
}
*{box-sizing:border-box;margin:0;padding:0}
html,body{width:710px;height:1200px;overflow:hidden;background:var(--white)}
body{font-family:"Open Sans",Arial,sans-serif;color:var(--ink);font-size:8px;position:relative}
.wrap{width:560px;margin:0 auto;position:relative}

/* header */
.site-header{background:var(--darker);height:54px}
.site-header .wrap{height:54px;display:flex;align-items:center;justify-content:space-between}
.brand{display:flex;align-items:center;gap:5px;color:var(--white);font-weight:800;font-size:17px;letter-spacing:.3px}
.brand-dot{width:9px;height:9px;background:var(--red)}
.main-nav{display:flex;gap:12px;margin-left:14px}
.main-nav a{color:var(--white);font-weight:700;font-size:8px;text-decoration:none}
.header-right{display:flex;flex-direction:column;align-items:flex-end;gap:6px}
.meta-links{display:flex;gap:12px;color:#bdbdbd;font-size:6.5px}
.meta-links .cart{color:var(--white);font-weight:700}
.search{display:flex;width:150px;height:15px;background:var(--white)}
.search span{flex:1;color:#999;font-size:6.5px;padding:3px 5px}
.search i{width:16px;background:var(--red)}

.cat-bar{background:var(--dark);height:16px;border-top:1px solid #333}
.cat-bar .wrap{display:flex;height:16px;align-items:center;gap:0}
.cat-bar a{color:#cfcfcf;font-size:6px;font-weight:600;padding:0 7px;line-height:16px;text-decoration:none;border-right:1px solid #3a3a3a}
.cat-bar a.best{background:var(--red);color:var(--white)}
.cat-bar a.sale{color:var(--red)}

.usp-bar{background:#3b3c40;height:18px}
.usp-bar .wrap{display:flex;justify-content:space-between;height:18px;align-items:center}
.usp{display:flex;align-items:center;gap:5px;color:var(--white);font-size:6.5px;font-weight:700}
.usp i{width:8px;height:8px;border-radius:50%;background:var(--red)}

/* hero */
.hero{margin-top:8px;height:232px;position:relative;
  background:linear-gradient(180deg,#7fa9d6 0%,#b7cde4 35%,#e9eef3 55%,#7b8a98 75%,#3d4650 100%)}
.hero-label{position:absolute;right:30px;top:26px;color:var(--ink);font-weight:800;font-size:20px;letter-spacing:1px}
.hero-badge{position:absolute;right:26px;bottom:38px;width:74px;height:74px;border-radius:50%;background:var(--red);color:var(--white);font-size:22px;font-weight:800;display:flex;align-items:center;justify-content:center}
.hero-dots{position:absolute;bottom:8px;left:50%;transform:translateX(-50%);display:flex;gap:4px}
.hero-dots i{width:5px;height:5px;border-radius:50%;background:#fff;opacity:.6}
.hero-dots i:first-child{opacity:1;background:var(--red)}

/* brand strip */
.brand-strip{display:flex;justify-content:space-between;align-items:center;height:40px;padding:0 10px;border-bottom:1px solid var(--line)}
.brand-strip span{font-weight:800;font-size:12px;color:#444;letter-spacing:.5px}

/* products */
.section-title{text-align:center;font-size:11px;font-weight:600;letter-spacing:1px;margin:12px 0 10px}
.products{display:flex;gap:12px;position:relative;padding:0 18px}
.arrow{position:absolute;top:40px;width:14px;height:22px;background:var(--light);display:flex;align-items:center;justify-content:center}
.arrow.prev{left:0}.arrow.next{right:0}
.card{flex:1;border:1px solid var(--line);text-align:center;padding-bottom:6px;position:relative}
.card .img{height:100px;margin:6px}
.card .new{position:absolute;top:0;right:0;background:#4a8fd6;color:#fff;font-size:5.5px;font-weight:700;padding:2px 4px}
.card .off{position:absolute;top:0;left:0;background:var(--red);color:#fff;font-size:5.5px;font-weight:700;padding:2px 4px}
.card h3{font-size:6.5px;font-weight:600;line-height:1.3;min-height:17px;padding:0 6px}
.price{color:var(--red);font-weight:800;font-size:10px;margin-top:4px}
.old{color:#999;font-size:6px;text-decoration:line-through}
.dots{display:flex;justify-content:center;gap:4px;margin:8px 0}
.dots i{width:5px;height:5px;border-radius:50%;background:#ccc}
.dots i:first-child{background:var(--red)}

/* teasers */
.teasers{display:flex;gap:10px}
.teaser{flex:1;height:108px;position:relative}
.teaser.climb{background:linear-gradient(135deg,#8b8f94,#c3c1bb 60%,#6d7176)}
.teaser.run{background:linear-gradient(135deg,#6f8ea8,#c9b79a 55%,#8a6f58)}
.teaser h4{position:absolute;top:10px;left:0;background:var(--red);color:#fff;font-size:9px;font-weight:800;padding:3px 8px}
.teaser .more{position:absolute;bottom:8px;left:8px;background:var(--darker);color:#fff;font-size:5.5px;padding:2px 5px}

/* dark band + newsletter */
.usp-band{background:var(--dark);height:20px;margin-top:10px}
.usp-band .wrap{display:flex;justify-content:space-between;height:20px;align-items:center}
.newsletter{background:var(--darker);height:108px;color:#d0d0d0}
.newsletter .wrap{display:flex;gap:20px;padding-top:12px}
.nl-text{width:250px}
.nl-text h5{color:#fff;font-size:7.5px;font-weight:800;margin-bottom:5px}
.nl-text p{font-size:6px;line-height:1.5;margin-bottom:5px}
.nl-form{flex:1}
.nl-offer{display:flex;background:#fff;height:38px;align-items:center}
.nl-offer b{background:var(--red);color:#fff;font-size:18px;width:50px;height:38px;display:flex;align-items:center;justify-content:center}
.nl-offer span{color:var(--ink);font-size:8px;font-weight:700;padding-left:10px}
.nl-input{display:flex;margin-top:8px;height:17px}
.nl-input span{flex:1;background:#fff;color:#999;font-size:6px;padding:4px 6px}
.nl-input em{background:var(--red);color:#fff;font-style:normal;font-size:6px;font-weight:700;padding:4px 8px}

/* footer */
.footer-cols{display:flex;gap:20px;padding-top:16px;height:150px}
.footer-cols div{flex:1}
.footer-cols h6{font-size:7px;font-weight:800;margin-bottom:6px}
.footer-cols li{list-style:none;font-size:6px;color:var(--grey);line-height:1.75}
.footer-cols p{font-size:6px;color:var(--grey);line-height:1.6}
.trust{display:flex;gap:20px;border-top:1px solid var(--line);padding-top:12px}
.trust h6{font-size:6.5px;font-weight:800;margin-bottom:8px}
.trust .seals{display:flex;gap:6px}
.seal{width:28px;height:28px;border-radius:50%;background:#d8d8d8}
.seal.sq{border-radius:2px;background:#c9c9c9}
.trust .names{display:flex;gap:12px;align-items:center;height:28px}
.trust .names span{font-weight:800;font-size:9px;color:#333}
.pay{margin-left:auto;display:flex;gap:10px;align-items:flex-end;height:44px}
.pay span{font-weight:800;font-size:9px;color:#2a3c78}
.copy{position:absolute;bottom:40px;left:75px;font-size:6px;color:var(--grey)}
</style>
</head>
<body>

<header class="site-header">
  <div class="wrap">
    <div style="display:flex;align-items:center">
      <div class="brand"><i class="brand-dot"></i>KitVarro.com</div>
      <nav class="main-nav"><a>HERREN</a><a>DAMEN</a><a>KINDER/JUGEND</a><a>GESCHENKIDEEN</a></nav>
    </div>
    <div class="header-right">
      <div class="meta-links"><span>Deutschland</span><span>Merkzettel</span><span>Mein Konto</span><span class="cart">0,00 €</span></div>
      <div class="search"><span>SUCHE</span><i></i></div>
    </div>
  </div>
</header>
<nav class="cat-bar">
  <div class="wrap">
    <a>OUTDOOR</a><a>KLETTERN</a><a>RUNNING</a><a>SKI</a><a>SNOWBOARD</a><a>ZWEIRAD</a><a>TENNIS</a><a>FREIZEIT</a><a class="best">BESTPREISE</a><a class="sale">%SALE</a>
  </div>
</nav>
<div class="usp-bar">
  <div class="wrap">
    <div class="usp"><i></i>EXPRESSLIEFERUNG</div>
    <div class="usp"><i></i>FINAL WINTER SALE BIS 70%</div>
    <div class="usp"><i></i>GRATIS RÜCKSENDUNG</div>
  </div>
</div>

<main class="wrap">
  <section class="hero" role="img" aria-label="Bergpanorama mit Outdoorjacken der Winterkollektion">
    <div class="hero-label">ALPVERO</div>
    <div class="hero-badge">-50%</div>
    <div class="hero-dots"><i></i><i></i><i></i><i></i></div>
  </section>

  <div class="brand-strip">
    <span>DRAVENA</span><span>ARDESA</span><span>CHELVO</span><span>LORETT</span><span>HAGMERE</span><span>SKORDAN</span>
  </div>

  <h2 class="section-title">TOP PRODUKTE</h2>
  <div class="products">
    <div class="arrow prev"><svg width="6" height="8"><path d="M5 0L1 4l4 4" stroke="#888" fill="none"/></svg></div>
    <article class="card"><span class="off">-21%</span><span class="new">NEU</span>
      <div class="img" role="img" aria-label="Laufschuh türkis" style="background:linear-gradient(135deg,#eef6f5,#7fd0c6)"></div>
      <h3>NORVIK FLOW 5.0 DAMEN LAUF-SCHUHE</h3><div class="price">94,99 €</div><div class="old">119,95 €</div></article>
    <article class="card"><span class="off">-12%</span><span class="new">NEU</span>
      <div class="img" role="img" aria-label="Sicherungsgerät grau" style="background:linear-gradient(135deg,#f4f4f4,#a9adb2)"></div>
      <h3>PERTIVA GRIPO 2 SICHERUNGS-GERÄT</h3><div class="price">57,75 €</div><div class="old">65,95 €</div></article>
    <article class="card"><span class="off">-20%</span><span class="new">NEU</span>
      <div class="img" role="img" aria-label="Enduro-Mountainbike" style="background:linear-gradient(135deg,#f6f6f6,#9aa37a)"></div>
      <h3>SKORDAN GENO LT 710 2015 ENDUROBIKE</h3><div class="price">3.999,99 €</div><div class="old">4.999,00 €</div></article>
    <article class="card"><span class="off">-14%</span><span class="new">NEU</span>
      <div class="img" role="img" aria-label="Downhill-Helm weiß" style="background:linear-gradient(135deg,#fafafa,#c8c8c8)"></div>
      <h3>PELKO CORVA DOWNHILL HELM</h3><div class="price">299,99 €</div><div class="old">349,95 €</div></article>
    <div class="arrow next"><svg width="6" height="8"><path d="M1 0l4 4-4 4" stroke="#888" fill="none"/></svg></div>
  </div>
  <div class="dots"><i></i><i></i><i></i></div>

  <div class="teasers">
    <div class="teaser climb" role="img" aria-label="Kletterer an einer Felswand"><h4>KLETTERN 2015</h4><span class="more">zu den NEUHEITEN</span></div>
    <div class="teaser run" role="img" aria-label="Trailläufer in den Bergen"><h4>RUNNING NEWS</h4><span class="more">jetzt entdecken</span></div>
  </div>
</main>

<div class="usp-band">
  <div class="wrap">
    <div class="usp"><i></i>EXPRESSLIEFERUNG</div>
    <div class="usp"><i></i>FINAL WINTER SALE BIS 70%</div>
    <div class="usp"><i></i>GRATIS RÜCKSENDUNG</div>
  </div>
</div>
<section class="newsletter">
  <div class="wrap">
    <div class="nl-text">
      <h5>NEWSLETTER ANMELDEN</h5>
      <p>... und ab sofort 5€ Rabatt auf Ihre nächste Bestellung ab einem Warenwert von 100€ sichern.</p>
      <p>Mit dem Newsletter erhalten Sie regelmäßig alle Neuheiten, Aktionen und exklusive Angebote aus unserem Shop direkt per E-Mail.</p>
    </div>
    <div class="nl-form">
      <div class="nl-offer"><b>5€</b><span>JETZT ANMELDEN UND 5 € SICHERN</span></div>
      <div class="nl-input"><span>Ihre E-Mail-Adresse</span><em>JETZT EINTRAGEN</em></div>
    </div>
  </div>
</section>

<footer class="wrap">
  <div class="footer-cols">
    <div><h6>FÜR KUNDEN</h6><ul>
      <li>Versand und Lieferung</li><li>Zahlungsmethoden</li><li>Rücksendung</li><li>Service | Hilfe | FAQ</li><li>Datenschutz</li><li>Empfehlungen &amp; Bildrechte</li><li>Gutscheine</li></ul></div>
    <div><h6>ÜBER KITVARRO.COM</h6><ul>
      <li>Über KitVarro.com</li><li>Unsere Shops in Deutschland</li><li>Jobs</li><li>Presse</li><li>Sitemap</li><li>Kontaktseite</li><li>Impressum</li></ul></div>
    <div><h6>DEALS OF KITVARRO.COM</h6>
      <p>Im KitVarro.com Onlineshop finden Sie Sportartikel und Ausrüstung für Outdoor, Klettern, Running, Ski und Radsport von über hundert Marken. Alle Produkte zeigen wir in 3D, damit Sie jedes Detail vor dem Kauf genau ansehen können. Schneller Versand, einfache Rücksendung und persönliche Beratung gehören bei uns selbstverständlich dazu.</p></div>
  </div>
  <div class="trust">
    <div><h6>GARANTIERT &amp; SICHER</h6><div class="seals"><i class="seal"></i><i class="seal sq"></i><i class="seal"></i></div></div>
    <div><h6>UNSERE TOP-MARKEN</h6><div class="names"><span>ALPVERO</span><span>ATROVA</span><span>GARVEL</span><span>NORVIK</span></div></div>
    <div class="pay"><span>VESTRA</span><span>MONDCARD</span><span>SOFALA</span><span>PAYMORA</span></div>
  </div>
</footer>
<div class="copy">©KitVarro.com | Kit Varro GmbH 2015</div>
</body>
</html>
```